plumbers buisness card

A buisness card for a plumbing buisness
needs to have a water theme with navy blue, light blue and white
with an image of either a water drop, pipes, tools or something relating to plumbing and incorperating my buisness name as a logo

"Kesterly Plumbing" is the words that need to stand out with "& gasfitting" to be smaller
Updates

spelling error on brief, "maintenance"
and also could you include my email m_kesterly@mailnest.com.au

Industry/Entity Type

Plumbing

Contact Information for Business Card

Kesterly Plumbing & Gasfitting

marcus kesterly
0493612085

specialising in
-new homes
-maitenance
-renovations

license no.
-73804

```html
<!DOCTYPE html>
<html lang="en">
<head>
<meta charset="utf-8">
<title>Kesterly Plumbing &amp; Gasfitting – Business Card</title>
<link rel="stylesheet" href="https://fonts.googleapis.com/css2?family=Special+Elite&family=Cabin:wght@400;500&display=swap">
<style>
  :root {
    --navy: #0b2c9c;
    --navy-ink: #132a8a;
    --card-blue: #45b0ec;
    --card-light: #62c2f3;
    --card-pale: #86d4f7;
    --wrench-top: #3d9ee3;
    --wrench-bottom: #3592dc;
    --stack-1: #3a9fe0;
    --stack-2: #56b8ee;
    --white: #ffffff;
  }
  * { margin: 0; padding: 0; box-sizing: border-box; }
  html, body { width: 1200px; height: 933px; overflow: hidden; }
  body {
    background: var(--navy);
    position: relative;
    font-family: "Cabin", sans-serif;
  }
  .card { position: absolute; overflow: hidden; background: var(--card-blue); }
  .card-stack { position: absolute; width: 341px; height: 543px; }
  .card-shape { position: absolute; left: 0; top: 0; }

  /* front */
  .stack-back-1 { left: 218px; top: 214px; background: var(--stack-1); }
  .stack-back-2 { left: 224px; top: 210px; background: var(--stack-2); }
  .card-front { left: 230px; top: 206px; width: 341px; height: 543px; }

  .logo {
    position: absolute;
    left: 88px; top: 146px;
    font-family: "Special Elite", monospace;
    font-size: 32px;
    line-height: 1.1;
    color: var(--navy-ink);
    white-space: nowrap;
  }
  .logo-tag {
    position: absolute;
    left: 90px; top: 222px;
    font-size: 17px;
    color: var(--navy-ink);
  }
  .services {
    position: absolute;
    left: 272px; top: 291px;
    transform-origin: 0 0;
    transform: rotate(90deg);
    font-size: 16px;
    line-height: 1.3;
    color: var(--navy-ink);
    white-space: nowrap;
  }

  /* back */
  .card-back { left: 615px; top: 200px; width: 331px; height: 532px; }
  .contact-name {
    position: absolute;
    left: 43px; top: 116px;
    font-size: 26px;
    color: var(--white);
  }
  .contact-phone {
    position: absolute;
    left: 102px; top: 155px;
    font-size: 19px;
    color: var(--navy-ink);
    letter-spacing: 0.5px;
  }
  .contact-license {
    position: absolute;
    left: 81px; top: 191px;
    font-size: 15px;
    color: var(--white);
  }
  .contact-email {
    position: absolute;
    left: 60px; top: 490px;
    transform-origin: 0 0;
    transform: rotate(-90deg);
    font-size: 16px;
    color: var(--navy-ink);
    white-space: nowrap;
  }
</style>
</head>
<body>

  <div class="card-stack stack-back-1"></div>
  <div class="card-stack stack-back-2"></div>

  <section class="card card-front">
    <svg class="card-shape" width="341" height="543" viewBox="0 0 341 543" aria-hidden="true">
      <rect x="0" y="0" width="341" height="205" fill="var(--card-light)"/>
      <rect x="212" y="205" width="82" height="338" fill="var(--card-pale)"/>
    </svg>
    <svg class="card-shape" width="341" height="543" viewBox="0 0 341 543" role="img" aria-label="Large pipe wrench illustration gripping a pipe">
      <defs>
        <linearGradient id="wrenchFront" x1="0" y1="0" x2="0" y2="1">
          <stop offset="0" stop-color="var(--wrench-top)" stop-opacity="0.35"/>
          <stop offset="1" stop-color="var(--wrench-bottom)" stop-opacity="0.7"/>
        </linearGradient>
      </defs>
      <rect x="20" y="20" width="200" height="510" rx="30" fill="url(#wrenchFront)"/>
    </svg>
    <div class="logo">Kesterly<br>Plumbing</div>
    <div class="logo-tag">&amp; Gas fitting</div>
    <div class="services">specializing in -new homes -<br>maintenance -renovations</div>
  </section>

  <section class="card card-back">
    <svg class="card-shape" width="331" height="532" viewBox="0 0 331 532" aria-hidden="true">
      <rect x="0" y="0" width="331" height="105" fill="var(--card-light)"/>
      <rect x="0" y="218" width="122" height="314" fill="var(--card-pale)"/>
    </svg>
    <svg class="card-shape" width="331" height="532" viewBox="0 0 331 532" role="img" aria-label="Pipe wrench illustration gripping a pipe">
      <defs>
        <linearGradient id="wrenchBack" x1="0" y1="0" x2="0" y2="1">
          <stop offset="0" stop-color="var(--wrench-top)" stop-opacity="0.35"/>
          <stop offset="1" stop-color="var(--wrench-bottom)" stop-opacity="0.7"/>
        </linearGradient>
      </defs>
      <rect x="130" y="20" width="186" height="500" rx="30" fill="url(#wrenchBack)"/>
    </svg>
    <div class="contact-name">Marcus Kesterly</div>
    <div class="contact-phone">0493612085</div>
    <div class="contact-license">license no. -73804</div>
    <div class="contact-email">email m_kesterly@mailnest.com.au</div>
  </section>

</body>
</html>
```